Vell Partners Building Business Cards

We need a business card that reflects our business as "Solar Experts" in San Diego. Browse our website www.vellpartners.example our License needs to be displayed as "CSLB# 4718392" our phone number is (619) 555-0147

Save thousands on your electric bills and increase the value of your home while helping to protect the environment. Our solar installation experts will help you design the system that's right for you, using only the highest quality equipment that will look great and give you ideal performance. Our goal is to make you energy independent, and get your electric bill to 0.

Tobias Wrenfield
(619) 555-0147
tobias@vellpartners.example

Target Market(s)

Home owners in san diego looking for solar

Industry/Entity Type

Solar Energy

Contact Information for Business Card

Tobias Wrenfield
(619) 555-0147
tobias@vellpartners.example

Font styles to use
Other font styles liked:
• Use our logo font

Requirements
Must have
• License needs to be displayed as "CSLB# 4718392" our phone number is (619) 555-0147
Nice to have
• Real images of rooftop home solar in san diego
Should not have
• our business address

```html
<!DOCTYPE html>
<html lang="en">
<head>
<meta charset="utf-8">
<title>Vell Partners Building — Business Card</title>
<link rel="stylesheet" href="https://fonts.googleapis.com/css2?family=Alegreya+Sans:wght@400;500&display=swap">
<style>
  :root {
    --brand-blue: #144a80;
    --paper: #ffffff;
    --sun-orange: #f6aa1c;
    --text-light: #ffffff;
  }
  * { margin: 0; padding: 0; box-sizing: border-box; }
  html, body {
    width: 1200px;
    height: 723px;
    overflow: hidden;
    background: var(--paper);
  }
  .card {
    position: relative;
    width: 1200px;
    height: 723px;
    background: var(--paper);
    font-family: "Alegreya Sans", "Trebuchet MS", sans-serif;
  }
  .card__panel {
    position: absolute;
    inset: 0;
    width: 1200px;
    height: 723px;
  }
  .card__panel polygon { fill: var(--brand-blue); }
  .contact {
    position: absolute;
    left: 52px;
    top: 208px;
    color: var(--text-light);
    list-style: none;
  }
  .contact__role {
    font-size: 30px;
    line-height: 1;
    font-weight: 400;
  }
  .contact__name {
    font-size: 39px;
    line-height: 1;
    font-weight: 400;
    margin-top: 22px;
    letter-spacing: 0.3px;
  }
  .contact__line {
    font-size: 31px;
    line-height: 1;
    margin-top: 22px;
  }
  .wordmark {
    position: absolute;
    left: 654px;
    top: 330px;
    display: flex;
    align-items: center;
    gap: 14px;
  }
  .wordmark__dot {
    width: 34px;
    height: 34px;
    border-radius: 50%;
    background: var(--sun-orange);
    flex: none;
  }
  .wordmark__name {
    font-size: 50px;
    font-weight: 500;
    line-height: 1;
    color: var(--brand-blue);
    white-space: nowrap;
  }
</style>
</head>
<body>
  <main class="card">
    <svg class="card__panel" viewBox="0 0 1200 723" aria-hidden="true">
      <polygon points="0,0 628,0 481,723 0,723"/>
    </svg>

    <ul class="contact">
      <li class="contact__role">Director</li>
      <li class="contact__name">Tobias Wrenfield</li>
      <li class="contact__line">Phone : (619) 555-0147</li>
      <li class="contact__line">Email : tobias@vellpartners.example</li>
      <li class="contact__line">Licesned : CSLB# 4718392</li>
    </ul>

    <div class="wordmark">
      <span class="wordmark__dot"></span>
      <span class="wordmark__name">Vell Partners Building</span>
    </div>
  </main>
</body>
</html>
```